Business Card Design - Law Firm

We are a boutique law firm located near the beach in Manly, Australia. We have recently had a new logo designed and are revamping our business cards with the new logo.

We have recently had a business card design done for us but are not entirely happy with it. We are looking for something modern, simplistic but striking. We would like to see multiple designs.

We have attached a word document which includes our new logo and the current business card design which we are looking at moving away from.

We would like the business cards to be double sided. We would like the design to include something which we can print in gloss colour when we send it to the business card printers.

```html
<!DOCTYPE html>
<html lang="en">
<head>
<meta charset="utf-8">
<title>Harwood &amp; Associates Lawyers – Business Card</title>
<link rel="stylesheet" href="https://fonts.googleapis.com/css2?family=Montserrat:wght@400;600&family=Lato:wght@400;700&display=swap">
<style>
  :root {
    --backdrop: #202124;
    --navy: #23398a;
    --royal: #3a55a8;
    --periwinkle: #7d95d0;
    --ink: #222633;
    --muted: #7a7f8c;
    --paper: #ffffff;
  }
  * { box-sizing: border-box; margin: 0; padding: 0; }
  html, body { width: 1200px; height: 900px; overflow: hidden; }
  body { background: var(--backdrop); position: relative; font-family: "Lato", sans-serif; }

  .card {
    position: absolute;
    width: 620px;
    height: 354px;
    box-shadow: 0 18px 40px rgba(0,0,0,0.45);
  }

  /* Front */
  .card-front {
    left: 100px; top: 80px;
    background: linear-gradient(30deg, var(--periwinkle) 0%, var(--royal) 55%, var(--navy) 100%);
    display: flex; flex-direction: column; align-items: center; justify-content: center;
    color: var(--paper);
  }
  .brand { display: flex; flex-direction: column; align-items: center; }
  .brand-row { display: flex; align-items: center; gap: 14px; }
  .brand-dot { width: 16px; height: 16px; border-radius: 50%; background: currentColor; }
  .brand-name {
    font-family: "Montserrat", sans-serif; font-weight: 600;
    font-size: 30px; letter-spacing: 1.5px; white-space: nowrap;
  }
  .brand-tag {
    font-family: "Montserrat", sans-serif; font-weight: 400;
    font-size: 13px; letter-spacing: 14px; margin-top: 8px; padding-left: 14px;
    opacity: 0.9;
  }

  /* Back */
  .card-back {
    left: 480px; top: 466px;
    background: var(--paper);
    border-bottom: 6px solid var(--royal);
  }
  .card-back .brand { position: absolute; top: 58px; left: 0; right: 0; color: var(--ink); }
  .card-back .brand-name { font-size: 24px; }
  .card-back .brand-dot { background: var(--royal); width: 13px; height: 13px; }
  .card-back .brand-tag { color: var(--muted); font-size: 11px; letter-spacing: 11px; }

  .holder { position: absolute; right: 34px; top: 168px; text-align: right; }
  .holder-name { color: var(--royal); font-weight: 700; font-size: 19px; letter-spacing: 0.3px; }
  .holder-role { color: var(--ink); font-size: 13px; margin-top: 2px; }
  .holder-address { color: var(--ink); font-weight: 700; font-size: 12.5px; margin-top: 26px; white-space: nowrap; }

  .contacts { position: absolute; left: 34px; bottom: 26px; list-style: none; }
  .contacts li {
    display: flex; align-items: center; gap: 10px;
    color: var(--ink); font-size: 13.5px; line-height: 24px; white-space: nowrap;
  }
  .contacts svg { width: 14px; height: 14px; flex: none; }
  .icon-solid { fill: var(--navy); }
  .icon-line { fill: none; stroke: var(--navy); stroke-width: 2; }
</style>
</head>
<body>

<section class="card card-front" aria-label="Card front">
  <div class="brand">
    <div class="brand-row">
      <span class="brand-dot"></span>
      <span class="brand-name">Harwood &amp; Associates</span>
    </div>
    <span class="brand-tag">LAWYERS</span>
  </div>
</section>

<section class="card card-back" aria-label="Card back">
  <div class="brand">
    <div class="brand-row">
      <span class="brand-dot"></span>
      <span class="brand-name">Harwood &amp; Associates</span>
    </div>
    <span class="brand-tag">LAWYERS</span>
  </div>

  <div class="holder">
    <p class="holder-name">Nadia Fellows</p>
    <p class="holder-role">Practise Manager</p>
    <p class="holder-address">Suite 4, 18 Pier Lane, BAYHAVEN VIC 3999</p>
  </div>

  <ul class="contacts">
    <li>
      <svg class="icon-solid" viewBox="0 0 24 24" aria-hidden="true"><path d="M6.6 10.8a15.1 15.1 0 0 0 6.6 6.6l2.2-2.2a1 1 0 0 1 1-.25 11.4 11.4 0 0 0 3.6.57 1 1 0 0 1 1 1V20a1 1 0 0 1-1 1A17 17 0 0 1 3 4a1 1 0 0 1 1-1h3.5a1 1 0 0 1 1 1c0 1.25.2 2.45.57 3.57a1 1 0 0 1-.25 1z"/></svg>
      (03) 9418 3076
    </li>
    <li>
      <svg class="icon-line" viewBox="0 0 24 24" aria-hidden="true"><path d="M2 5h20v14H2z M3.5 6.5 12 13l8.5-6.5"/></svg>
      nadia.fellows@harwoodandassociates.com.au
    </li>
    <li>
      <svg class="icon-line" viewBox="0 0 24 24" aria-hidden="true"><circle cx="12" cy="12" r="9"/><path d="M3 12h18M12 3c3 3 3 15 0 18M12 3c-3 3-3 15 0 18" stroke-width="1.6"/></svg>
      www.harwoodandassociates.com.au
    </li>
  </ul>
</section>

</body>
</html>
```